Melissa Tarnow Personal Business Card

I like orange. It's would better if my card have an orange background
Address: 4720 Halberd Lane #318
San Jose
California
US
Tel: 4085172946

Industry/Entity Type

Business

```html
<!DOCTYPE html>
<html lang="en">
<head>
<meta charset="utf-8">
<title>Business Card</title>
<link rel="stylesheet" href="https://fonts.googleapis.com/css2?family=Arimo:wght@400;700&display=swap">
<style>
  :root {
    --page-bg: #e8e5e1;
    --orange: #f5821f;
    --orange-light: #f7a063;
    --charcoal: #3a393b;
    --charcoal-light: #4d4c4f;
    --rule: #4a4340;
    --white: #ffffff;
  }
  * { margin: 0; padding: 0; box-sizing: border-box; }
  html, body {
    width: 1200px;
    height: 970px;
    overflow: hidden;
    background: var(--page-bg);
    font-family: "Arimo", Arial, sans-serif;
  }
  .business-card {
    position: absolute;
    left: 100px;
    top: 207px;
    width: 1000px;
    height: 556px;
    overflow: hidden;
    color: var(--white);
    background:
      linear-gradient(100deg,
        var(--orange-light) 0%,
        #f6954a 25%,
        var(--orange) 45%,
        var(--orange) 70%,
        #f6914a 100%);
    box-shadow: 0 12px 30px rgba(0,0,0,0.18);
  }
  .contact-phone {
    position: absolute;
    right: 80px;
    top: 194px;
    text-align: right;
  }
  .field-label {
    display: block;
    font-weight: 700;
    font-size: 27px;
    line-height: 36px;
  }
  .field-value {
    display: block;
    font-weight: 400;
    font-size: 27px;
    line-height: 37px;
  }
  .divider {
    position: absolute;
    left: 77px;
    right: 80px;
    top: 292px;
    height: 3px;
    background: var(--rule);
  }
  .contact-address {
    position: absolute;
    left: 77px;
    top: 325px;
  }
  .footer-bands {
    position: absolute;
    left: 0;
    top: 0;
    width: 1000px;
    height: 556px;
  }
</style>
</head>
<body>
  <div class="business-card">
    <svg class="footer-bands" viewBox="0 0 755 420" preserveAspectRatio="none" aria-hidden="true">
      <defs>
        <linearGradient id="band-shade" x1="0" y1="0" x2="1" y2="0">
          <stop offset="0" stop-color="var(--charcoal)"/>
          <stop offset="0.55" stop-color="var(--charcoal-light)"/>
          <stop offset="1" stop-color="var(--charcoal)"/>
        </linearGradient>
      </defs>
      <path d="M0 359 H375 L402 386 H755 V420 H0 Z" fill="url(#band-shade)"/>
      <path d="M388 368 H755 V382 H402 Z" fill="var(--white)"/>
    </svg>

    <div class="contact-phone">
      <span class="field-label">Phone:</span>
      <span class="field-value">408.517.2946</span>
    </div>

    <div class="divider"></div>

    <div class="contact-address">
      <span class="field-label">Address:</span>
      <span class="field-value">4720 Halberd Lane #318</span>
      <span class="field-value">San Jose, California, US</span>
    </div>
  </div>
</body>
</html>
```